TRV Flyer

We need a professional design for flyers that we produce. The attached event draft is typical of the majority of flyers we will produce, and is the one that we need to do right now.

We would also like the source files for the design. We don’t have Corel Draw, but can work with any files produced in Adobe Creative Suite products.

Target Market(s)

Owners of residential apartments

Industry/Entity Type

Non-Profit

Requirements
Must have
• Design must be complimentary to our new website design at www.trv.org.au so we can establish consistent branding.
• Any fonts used must be freely avalaible standard fonts used in Microsoft Word

```html
<!DOCTYPE html>
<html lang="en">
<head>
<meta charset="utf-8">
<title>TRV Educational Workshop</title>
<link href="https://fonts.googleapis.com/css2?family=Arimo:ital,wght@0,400;0,700;1,400&display=swap" rel="stylesheet">
<style>
  :root {
    --navy: #263f95;
    --gold: #8a7745;
    --panel: #e4e0d9;
    --ink: #1a1a1a;
    --dot: #8a8a8a;
    --paper: #ffffff;
  }
  * { margin: 0; padding: 0; box-sizing: border-box; }
  html, body { width: 848px; height: 1200px; overflow: hidden; background: var(--paper); }
  body { font-family: "Arimo", Arial, sans-serif; color: var(--ink); position: relative; }

  .top-band { position: absolute; left: 11px; top: 11px; width: 810px; height: 30px; background: var(--navy); }
  .gold-rule { position: absolute; left: 11px; top: 44px; width: 810px; height: 4px; background: var(--gold); }
  .hero { position: absolute; left: 11px; top: 51px; width: 810px; height: 436px;
    background: linear-gradient(180deg, #0e1f6b 0%, #1d2c7a 35%, #4a3a2a 70%, #1a1a22 100%); }

  .side-panel { position: absolute; left: 11px; top: 497px; width: 263px; height: 668px; background: var(--panel); padding: 0 16px; }
  .brand { display: flex; align-items: center; gap: 10px; margin: 36px 0 0 14px; }
  .brand-mark { width: 38px; height: 38px; background: var(--navy); }
  .brand-name { color: var(--navy); font-size: 15px; line-height: 16px; letter-spacing: 1px; text-transform: uppercase; }
  .dots { border-top: 1.5px dotted var(--dot); }
  .side-panel .dots { margin: 0 0 0 10px; width: 232px; }
  .side-panel .dots.first { margin-top: 30px; }
  .info { margin-left: 10px; }
  .info h3 { color: var(--navy); font-size: 15px; font-weight: 700; margin-top: 18px; }
  .info p { color: var(--gold); font-size: 15px; font-weight: 700; line-height: 21px; margin-top: 2px; }
  .info .dates { font-size: 14.5px; line-height: 17.5px; }
  .cta { margin: 24px 0 22px 10px; color: var(--navy); font-weight: 700; font-size: 15px; line-height: 25.3px; text-transform: uppercase; }
  .register { margin-left: 10px; width: 232px; text-align: center; color: var(--gold); font-weight: 700; font-size: 15px; padding: 10px 0 9px; border-top: 1.5px dotted var(--dot); border-bottom: 1.5px dotted var(--dot); }

  .main { position: absolute; left: 285px; top: 502px; width: 526px; }
  .main h1 { color: var(--gold); font-size: 32px; font-weight: 700; letter-spacing: -0.2px; }
  .subtitle { color: var(--navy); font-size: 13.5px; margin-top: 4px; }
  .main .dots { margin-top: 12px; }
  .main h2 { color: var(--navy); font-size: 14px; font-weight: 700; margin-top: 13px; }
  .audience { list-style: none; font-size: 13.5px; line-height: 19.5px; margin-top: 6px; }
  .audience li { padding-left: 9px; text-indent: -9px; }
  .audience li::before { content: "• "; }
  .main h2.section { margin-top: 14px; }
  .body-copy { font-size: 13.6px; line-height: 17px; margin-top: 4px; }
  .theme { margin-top: 6px; padding-left: 1px; }
  .gap { margin-top: 26px; }

  .programme-table { position: absolute; left: 329px; top: 1009px; width: 450px; border-collapse: collapse; font-size: 12.5px; }
  .programme-table td, .programme-table th { border: 1.5px dotted var(--dot); padding: 3px 5px; text-align: left; vertical-align: middle; }
  .programme-table th { color: var(--navy); font-size: 13px; font-weight: 700; height: 24px; }
  .programme-table td { height: 21px; }
  .programme-table .tall td { height: 36px; }
  .period { color: var(--gold); font-weight: 700; width: 74px; }
  .topic { font-style: italic; width: 89px; }
  .bottom-rule { position: absolute; left: 285px; top: 1164px; width: 526px; border-top: 1.5px dotted var(--dot); }
</style>
</head>
<body>
  <div class="top-band"></div>
  <div class="gold-rule"></div>
  <div class="hero" role="img" aria-label="Night photograph of a city skyline with lit office towers above a river and bridge"></div>

  <aside class="side-panel">
    <div class="brand">
      <div class="brand-mark"></div>
      <div class="brand-name">Tenant<br>Residents<br>Voice</div>
    </div>
    <div class="dots first"></div>
    <div class="info">
      <h3>Location:</h3>
      <p>Wattle Point Club<br>24 Bayside Terrace<br>Cove Heights 2061</p>
      <h3>Dates:</h3>
      <p class="dates">The workshop will run twice –<br>on 12th June &amp; 26th June 2010</p>
      <h3>Time:</h3>
      <p>10.00 am to 4.00 pm.</p>
      <h3>Cost:</h3>
      <p>$60.00, which includes morning tea and lunch.</p>
    </div>
    <div class="dots" style="margin-top:20px"></div>
    <div class="cta">Enroll now -<br>Learn a lot -<br>Have some fun as well -<br>Share experiences -<br>Find out how TRV<br>can help you<br>in the longer term.</div>
    <div class="register">Register at www.trv.org.au</div>
  </aside>

  <main class="main">
    <h1>TRV Educational Workshop</h1>
    <p class="subtitle">“The Essentials of Strata Living – What Every Owner Needs to Know”</p>
    <div class="dots"></div>
    <h2>This workshop is for owners in strata apartments who want to learn more about</h2>
    <ul class="audience">
      <li>getting the best out of apartment living</li>
      <li>protecting their home and their investment AND particularly for</li>
      <li>executive committee members to know their rights and responsibilities in managing their strata scheme</li>
    </ul>
    <h2 class="section">Programme:</h2>
    <p class="body-copy">The day will comprise four sessions, each facilitated by a specialist. In each session the speaker will provide relevant information and set the topics for group work; participants will break into groups and work up solutions to each topic; and the groups will compare outcomes.</p>
    <h2 class="section gap">The day’s theme will be:</h2>
    <p class="body-copy theme">Gina is a new owner in her building called Utopia Tower. She notices some management processes which to her seem strange. She is elected to the executive committee and finds that the developer has retained more control than she realised - the service providers have long-term and onerous contracts, and she doesn’t seem to be able to exert enough influence. What does the law require her to do, as a committee member? How does she influence good management processes? The finances seem to be out of control, so how can she fix them so she doesn’t pay inflated levies each year and lose value on her investment? ... and then the neighbour above her apartment installs atimber floor and she has noise problems ... and the building seems to have a lot of defects</p>
  </main>

  <table class="programme-table">
    <tr><th></th><th>Topic</th><th>Speaker</th></tr>
    <tr><td class="period">Morning</td><td class="topic">Governance</td><td>Martin Hale, strata lawyer</td></tr>
    <tr class="tall"><td></td><td class="topic">Management</td><td>Peter Lowell, seasoned former chairperson &amp; executive committee member</td></tr>
    <tr><td class="period">Afternoon</td><td class="topic">Financials</td><td>David Brennan, accountant</td></tr>
    <tr><td></td><td class="topic">Physicality</td><td>Simon Carrera, facilities manager</td></tr>
  </table>
  <div class="bottom-rule"></div>
</body>
</html>
```